Breezeway Comfort business cards design

Need a business card design for a Heating and Air Conditioning business. I need these items included.
Business name: Breezeway Comfort
Owner: Marcus Tollefsen
License # 2874590
Phone number # 555-382-4071
Email: breezewaycomfortair@mailvista.example
Sales
Service
Installation
Maintenance

Heating and Air Conditioning

Requirements
Must have
• Company name , license number , phone number , email

```html
<!DOCTYPE html>
<html lang="en">
<head>
<meta charset="UTF-8">
<title>Breezeway Comfort – Business Cards</title>
<link href="https://fonts.googleapis.com/css2?family=Archivo:wght@400;600;700;800&display=swap" rel="stylesheet">
<style>
  :root {
    --bg: #2b2b2b;
    --blue: #2c55aa;
    --blue-light: #4a72bd;
    --blue-dark: #1f4597;
    --orange: #ef6a2a;
    --white: #ffffff;
    --ink: #1a1a1a;
    --grey: #555555;
    --product: #d9dde3;
  }
  * { margin: 0; padding: 0; box-sizing: border-box; }
  html, body {
    width: 1200px; height: 800px; overflow: hidden;
    background: var(--bg);
    font-family: "Archivo", Arial, sans-serif;
  }
  .stage {
    width: 1200px; height: 800px;
    display: flex; align-items: center; justify-content: center; gap: 40px;
  }
  .card {
    position: relative; width: 520px; height: 300px;
    border-radius: 16px; overflow: hidden;
  }

  /* Front */
  .card--front {
    background: linear-gradient(135deg, var(--blue-light) 0%, var(--blue) 55%, var(--blue-dark) 100%);
    color: var(--white);
  }
  .front-band {
    position: absolute; left: 0; right: 0; top: 150px; height: 70px;
    background: var(--white);
  }
  .front-brand {
    position: absolute; top: 54px; left: 0; right: 0;
    display: flex; align-items: center; justify-content: center; gap: 12px;
  }
  .front-brand__dot {
    width: 18px; height: 18px; border-radius: 50%; background: var(--white);
  }
  .front-brand__name {
    font-weight: 800; font-size: 30px; letter-spacing: 2px; text-transform: uppercase;
  }
  .front-products {
    position: absolute; left: 150px; top: 118px; width: 220px; height: 100px;
    border-radius: 8px;
    background: linear-gradient(180deg, #f2f4f7 0%, var(--product) 100%);
  }
  .front-services {
    position: absolute; left: 0; right: 0; bottom: 28px;
    display: flex; justify-content: center; gap: 12px;
    font-weight: 600; font-size: 13px; letter-spacing: 0.5px; text-transform: uppercase;
  }
  .front-services__sep { opacity: 0.9; }

  /* Back */
  .card--back { background: var(--white); }
  .edge { position: absolute; left: 0; right: 0; height: 6px; display: flex; }
  .edge--top { top: 0; }
  .edge--bottom { bottom: 0; }
  .edge span { display: block; height: 100%; }
  .edge .is-orange { background: var(--orange); }
  .edge .is-blue { background: var(--blue); }

  .back-brand {
    position: absolute; left: 40px; top: 140px; width: 170px;
    display: flex; flex-direction: column; align-items: flex-start; gap: 10px;
  }
  .back-brand__dot { width: 18px; height: 18px; border-radius: 50%; background: var(--orange); }
  .back-brand__name {
    font-weight: 800; font-size: 22px; line-height: 1.1; letter-spacing: 1px;
    color: var(--blue); text-transform: uppercase;
  }

  .back-details { position: absolute; left: 240px; top: 62px; white-space: nowrap; }
  .back-details__company {
    font-weight: 800; font-size: 17px; color: var(--blue); text-transform: uppercase; letter-spacing: 0.3px;
  }
  .back-details__name {
    font-weight: 700; font-size: 20px; color: var(--orange); margin-top: 2px;
  }
  .back-details__role {
    display: flex; align-items: center; gap: 8px; margin-top: 4px;
    font-weight: 800; font-size: 12px; color: var(--ink);
  }
  .back-details__role::after {
    content: ""; width: 32px; height: 1px; background: var(--ink);
  }
  .contact { list-style: none; margin-top: 22px; }
  .contact li {
    display: flex; align-items: center; gap: 8px;
    font-size: 11px; color: var(--grey); margin-bottom: 8px;
  }
  .contact svg { flex: none; }
</style>
</head>
<body>
<main class="stage">
  <section class="card card--front">
    <div class="front-band"></div>
    <div class="front-brand">
      <span class="front-brand__dot"></span>
      <span class="front-brand__name">Breezeway Comfort</span>
    </div>
    <div class="front-products" role="img" aria-label="Photo of a portable heater and a wall-mounted air conditioner unit"></div>
    <div class="front-services">
      <span>Sales</span><span class="front-services__sep">|</span>
      <span>Service</span><span class="front-services__sep">|</span>
      <span>Installation</span><span class="front-services__sep">|</span>
      <span>Maintenance</span>
    </div>
  </section>

  <section class="card card--back">
    <div class="edge edge--top"><span class="is-orange" style="width:45%"></span><span class="is-blue" style="width:55%"></span></div>

    <div class="back-brand">
      <span class="back-brand__dot"></span>
      <span class="back-brand__name">Breezeway<br>Comfort</span>
    </div>

    <div class="back-details">
      <p class="back-details__company">Breezeway Comfort</p>
      <p class="back-details__name">Marcus Tollefsen</p>
      <p class="back-details__role">OWNER</p>
      <ul class="contact">
        <li>
          <svg width="16" height="16" viewBox="0 0 16 16" aria-hidden="true">
            <rect width="16" height="16" rx="2" fill="var(--orange)"/>
            <path d="M5 3.5h2l1 2.5-1.3 1a6 6 0 0 0 2.3 2.3l1-1.3 2.5 1v2a1 1 0 0 1-1 1A8 8 0 0 1 4 4.5a1 1 0 0 1 1-1z" fill="#fff"/>
          </svg>
          555-382-4071
        </li>
        <li>
          <svg width="16" height="16" viewBox="0 0 16 16" aria-hidden="true">
            <rect width="16" height="16" rx="2" fill="var(--orange)"/>
            <path d="M3 8.2 13 3.5 10.5 13 8 9.5z" fill="#fff"/>
          </svg>
          breezewaycomfortair@mailvista.example
        </li>
        <li>
          <svg width="16" height="16" viewBox="0 0 16 16" aria-hidden="true">
            <rect width="16" height="16" rx="2" fill="var(--orange)"/>
            <rect x="4.5" y="3" width="7" height="10" rx="1" fill="#fff"/>
            <rect x="6" y="5.5" width="4" height="1" fill="var(--orange)"/>
            <rect x="6" y="8" width="4" height="1" fill="var(--orange)"/>
          </svg>
          2874590
        </li>
      </ul>
    </div>

    <div class="edge edge--bottom"><span class="is-blue" style="width:58%"></span><span class="is-orange" style="width:42%"></span></div>
  </section>
</main>
</body>
</html>
```